依頼詳細
ポスティング用のチラシです。
思わず手に取って見たくなるようなデザインとキャッチャーなコピーを
ご提案ください。

原稿にイラストを入れましたが、写真でも構いません。
また、全体のレイアウトも自由に変更頂いて構いません。

尚、コンペで表面が決まりましたら、裏面に着手していただきますので、
ご承知おきください。

それではご提案お待ちしております。
何卒よろしくお願い申し上げます。

記載項目
原稿にまとめました
サイズ
A4
ページ数
両面
希望イメージ
シンプル 複雑
単色 カラフル
暗い 明るい
日常 高級
遊び心 厳粛
未来的 伝統的
女性的 男性的
希望する色
納品ファイル
• イラストレーター形式 (.ai)
補足説明
お世話様でございます。
どれも素晴らしいご提案、誠にありがとうございました。
検討させていただきますので、決定までにしばらくお時間くださいませ。
宜しくお願い申し上げます。
■ 選んだ理由

インパクトのあるアイキャッチ(イラスト・コピー)と、非常に分かり易くまとめて頂いた所が
ポイントです。

■ 提案者全員のお礼・コメント

この度は素晴らしい作品をご提案頂きまして、誠にありがとうございました。
また機会を作りますので、今後ともよろしくお願い申し上げます。

```html
<!DOCTYPE html>
<html lang="ja">
<head>
<meta charset="utf-8">
<title>めがねのポケット 出張メガネ販売</title>
<link href="https://fonts.googleapis.com/css2?family=M+PLUS+Rounded+1c:wght@500;700;800;900&family=Noto+Sans+JP:wght@400;500;700;900&display=swap" rel="stylesheet">
<style>
:root{
  --cream:#f7f1de;
  --cream-deep:#efe5c6;
  --orange:#e8582a;
  --orange-soft:#f4a25a;
  --brown:#4a3726;
  --green:#7bb83a;
  --green-light:#e7f2d3;
  --green-dark:#4e8a22;
  --white:#ffffff;
  --grey:#8d8577;
}
*{margin:0;padding:0;box-sizing:border-box}
html,body{width:878px;height:1200px;overflow:hidden;background:var(--white)}
body{font-family:"Noto Sans JP",sans-serif;color:var(--brown)}
.flyer{position:relative;width:878px;height:1200px;background:var(--cream);overflow:hidden}
.abs{position:absolute}
.ph{position:absolute;border-radius:10px}
.brand{display:flex;align-items:center;gap:10px;font-family:"M PLUS Rounded 1c",sans-serif;font-weight:800;color:var(--brown)}
.brand-dot{width:22px;height:22px;border-radius:50%;background:var(--orange)}
.top-brand{left:0;right:0;top:18px;justify-content:center;font-size:30px}
.catch-1{left:0;right:0;top:66px;text-align:center;font-family:"M PLUS Rounded 1c",sans-serif;font-weight:900;font-size:48px;color:var(--orange);letter-spacing:2px}
.catch-2{left:0;right:0;top:122px;text-align:center;font-family:"M PLUS Rounded 1c",sans-serif;font-weight:900;font-size:56px;color:var(--brown);letter-spacing:1px}
.catch-side{left:120px;top:72px;writing-mode:vertical-rl;font-size:15px;font-weight:700;color:var(--orange)}
.lead{left:0;right:0;top:196px;text-align:center;font-size:14px;font-weight:500}
.label-here{left:300px;top:236px;font-size:16px;font-weight:700}
.bubble{position:absolute;border-radius:24px;font-family:"M PLUS Rounded 1c",sans-serif;font-weight:800;line-height:1.5}
.bubble-left{left:22px;top:258px;width:210px;height:210px;background:var(--white);border:3px solid var(--orange-soft);padding:28px 18px;font-size:21px;text-align:center}
.bubble-right{left:640px;top:222px;width:218px;height:250px;background:var(--green-light);border:3px solid var(--green);padding:18px 14px;font-size:18px;text-align:center;color:var(--green-dark)}
.bubble-right p+p{margin-top:14px;font-size:16px;color:var(--brown)}
.section-tag{position:absolute;background:var(--orange);color:var(--white);font-family:"M PLUS Rounded 1c",sans-serif;font-weight:800;font-size:17px;padding:5px 16px;border-radius:18px}
.step-text{position:absolute;display:flex;gap:8px;align-items:flex-start;font-size:14px;font-weight:700;line-height:1.4}
.step-num{flex:none;width:28px;height:28px;border-radius:50%;background:var(--green);color:var(--white);font-size:17px;display:flex;align-items:center;justify-content:center}
.band{left:0;right:0;top:668px;height:40px;background:var(--green);color:var(--white);font-weight:700;font-size:18px;text-align:center;line-height:40px}
.voice{position:absolute;left:150px;width:410px;font-size:13px;line-height:1.55}
.voice h3{font-size:16px;color:var(--orange);font-weight:900;margin-bottom:4px}
.footer{left:0;right:0;top:920px;bottom:0;background:var(--white);border-top:6px solid var(--orange-soft)}
.footer-card{left:22px;top:936px;width:400px;height:240px;border:3px solid var(--orange);border-radius:16px;background:var(--white);padding:18px 22px}
.footer-card .note{font-size:13px;color:var(--orange);font-weight:700}
.footer-card .company{font-size:16px;font-weight:700;margin-top:10px}
.footer-card .brand{font-size:32px;margin-top:2px}
.footer-card .addr{font-size:13px;margin-top:4px}
.tel{display:flex;align-items:center;gap:10px;margin-top:14px;font-family:"M PLUS Rounded 1c",sans-serif;font-weight:900;font-size:42px;color:var(--orange)}
.tags{left:452px;top:958px;display:flex;flex-direction:column;gap:8px}
.tags span{display:block;background:var(--green);color:var(--white);font-weight:700;font-size:16px;padding:4px 14px;border-radius:6px;text-align:center;width:112px}
.free{left:590px;top:950px;font-family:"M PLUS Rounded 1c",sans-serif;font-weight:900;font-size:96px;color:var(--orange);line-height:1}
.free-note{left:452px;top:1086px;width:400px;font-size:14px;line-height:1.6;font-weight:500}
</style>
</head>
<body>
<div class="flyer">
  <div class="brand top-brand abs"><span class="brand-dot"></span>めがねのポケット</div>
  <div class="catch-side abs">お電話一本で</div>
  <div class="catch-1 abs">安心をデリバリー</div>
  <div class="catch-2 abs">メガネも自宅で買う時代</div>
  <p class="lead abs">メガネが欲しいけれど外出が不安で、お店に行けない…そんなお悩みを解決！</p>
  <p class="label-here abs">めがねのポケットなら</p>

  <div class="ph" role="img" aria-label="ソファに座る高齢のご夫婦のイラスト" style="left:250px;top:262px;width:380px;height:250px;background:radial-gradient(ellipse at 50% 60%,#e9d6b4,#d9c5a0 60%,var(--cream) 100%)"></div>

  <div class="bubble bubble-left">わざわざお店に<br>行かなくても<br>もう大丈夫！<br>おウチで<br>待ってるだけ！</div>
  <div class="bubble bubble-right">
    <p>専用車でご自宅まで<br>うかがいます！</p>
    <p>ご注文後は会社や<br>ご自宅まで<br>ご購入後お届けします！</p>
  </div>
  <div class="ph" role="img" aria-label="スタッフの写真" style="left:745px;top:392px;width:100px;height:72px;background:linear-gradient(#cfd6d8,#9fa9ad)"></div>

  <span class="section-tag" style="left:26px;top:470px">ご購入まで</span>
  <div class="ph" role="img" aria-label="視力測定車の写真" style="left:26px;top:505px;width:240px;height:100px;background:linear-gradient(#eef1f3,#c9d0d6)"></div>
  <div class="ph" role="img" aria-label="自宅での視力検査の写真" style="left:290px;top:505px;width:150px;height:100px;background:linear-gradient(#e5d9c6,#bfae92)"></div>
  <div class="ph" role="img" aria-label="メガネフレームの写真" style="left:600px;top:505px;width:250px;height:100px;background:linear-gradient(#f3eee4,#d9cdb7)"></div>
  <div class="step-text" style="left:26px;top:615px;width:260px"><span class="step-num">1</span>視力測定車でご自宅に訪問</div>
  <div class="step-text" style="left:290px;top:615px;width:200px"><span class="step-num">2</span>自宅で視力検査</div>
  <div class="step-text" style="left:560px;top:615px;width:300px"><span class="step-num">3</span>レンズ・フレームをお選びいただきます</div>

  <div class="band abs">レンズメーカーは、男性用・女性用など各種豊富に取り揃えています。</div>

  <span class="section-tag" style="left:26px;top:722px">お客様の声</span>
  <div class="ph" role="img" aria-label="お客様の写真" style="left:30px;top:760px;width:105px;height:60px;background:linear-gradient(#e7dccb,#c8b79c)"></div>
  <div class="voice" style="top:756px">
    <h3>長野市A様／60代（女性）</h3>
    <p>免許を返納してから外出が減り、自宅で選べてとても助かりました。丁寧な説明で安心できました。</p>
  </div>
  <div class="ph" role="img" aria-label="お客様の写真" style="left:30px;top:840px;width:105px;height:60px;background:linear-gradient(#e7dccb,#c8b79c)"></div>
  <div class="voice" style="top:836px">
    <h3>長野市B様／70代（男性）</h3>
    <p>足が悪くお店に行けませんでしたが、家まで来てくれて検査も本格的。新しいメガネで毎日が明るくなりました。</p>
  </div>
  <div class="ph" role="img" aria-label="笑顔の高齢ご夫婦の写真" style="left:580px;top:740px;width:272px;height:165px;background:linear-gradient(#eef0e6,#c9cdb8)"></div>

  <div class="footer abs"></div>
  <div class="footer-card abs">
    <p class="note">メガネのことなら何でもご相談ください！</p>
    <p class="company">株式会社ミルネ</p>
    <div class="brand"><span class="brand-dot"></span>めがねのポケット</div>
    <p class="addr">長野市青葉町215</p>
    <div class="tel">
      <svg width="38" height="38" viewBox="0 0 24 24" aria-hidden="true"><path fill="#e8582a" d="M6.6 10.8a15.1 15.1 0 0 0 6.6 6.6l2.2-2.2a1 1 0 0 1 1-.25 11.4 11.4 0 0 0 3.6.57 1 1 0 0 1 1 1V20a1 1 0 0 1-1 1A17 17 0 0 1 3 4a1 1 0 0 1 1-1h3.5a1 1 0 0 1 1 1c0 1.25.2 2.45.57 3.57a1 1 0 0 1-.25 1z"/></svg>
      0120-00-4417
    </div>
  </div>
  <div class="tags abs"><span>視力検査</span><span>出張費</span><span>送料</span></div>
  <div class="free abs">無料</div>
  <p class="free-note abs">感染対策強化中！ご自宅への訪問の際は<br>しっかり感染対策したスタッフが伺います！</p>
</div>
</body>
</html>
```